13 Tovi - new website design project

Our company Tovi Electrical is developing a new lead generation website focused on Electrical, LED Lighting and Solar Power. We need a high converting website.

Example of our current website is www.tovielectrical.com.au You can take content from this website for this new design. Our colours are red, black and white. For our new website we would like to promote Tovi, Bright Days Ahead. Please listen to the jingle.

The below link is the company jingle that we have developed.
http://www.tunecraftstudio.com.au/tov-tc-v1/

The key for this brief is to generate leads for Electrical, LED Lighting (for commercial) and Solar Power & Storage.

Target Market(s)

Business owners in Melbourne Victoria

Number of Pages Required

4 page

Colors
ec1f27
ffffff

Requirements
Must have
• This page must be clean, be in line with company branding and a high converting lead website.

```html
<!DOCTYPE html>
<html lang="en">
<head>
<meta charset="utf-8">
<title>Tovi Electrical</title>
<link rel="stylesheet" href="https://fonts.googleapis.com/css2?family=Roboto:wght@300;400;500;700&family=Roboto+Condensed:wght@400;700&display=swap">
<style>
  :root {
    --red: #ec1f27;
    --black: #1b1b1b;
    --white: #ffffff;
    --grey-band: #f3f3f4;
    --night-top: #1c2b5a;
    --night-mid: #2a3a6e;
    --night-low: #3b3324;
    --hero-text: #ffffff;
  }
  * { box-sizing: border-box; margin: 0; padding: 0; }
  html, body { width: 1200px; height: 676px; overflow: hidden; background: var(--white); }
  body { font-family: "Roboto", Arial, sans-serif; color: var(--black); }

  .site { position: relative; width: 1200px; height: 676px; }

  .site-header {
    height: 76px;
    border-top: 3px solid var(--red);
    display: flex; align-items: center;
    padding: 0 48px;
    background: var(--white);
  }
  .brand { display: flex; align-items: center; gap: 10px; width: 320px; }
  .brand-mark { width: 22px; height: 22px; background: var(--red); }
  .brand-name { font-family: "Roboto Condensed", Arial, sans-serif; font-weight: 700; font-size: 28px; color: var(--black); }

  .main-nav { display: flex; gap: 38px; font-size: 14px; font-weight: 500; margin-left: 40px; }
  .main-nav a { color: var(--black); text-decoration: none; }

  .header-actions { margin-left: auto; display: flex; align-items: center; gap: 36px; }
  .chat-link { font-size: 14px; font-weight: 500; display: flex; align-items: center; gap: 5px; color: var(--black); }
  .call-button {
    background: var(--red); color: var(--white);
    font-family: "Roboto Condensed", Arial, sans-serif; font-weight: 700; font-size: 14px;
    padding: 7px 10px; border-radius: 4px;
  }

  .hero { position: relative; height: 426px; overflow: hidden; }
  .hero-photo {
    position: absolute; inset: 0;
    background: linear-gradient(180deg, var(--night-top) 0%, var(--night-mid) 45%, #4a4535 72%, var(--night-low) 100%);
  }
  .hero-shade {
    position: absolute; inset: 0;
    background: linear-gradient(115deg, rgba(0,0,0,0) 58%, rgba(255,255,255,0.06) 58%);
  }
  .hero-circle {
    position: absolute; left: 50%; top: 50%;
    width: 300px; height: 300px; margin: -150px 0 0 -150px;
    border-radius: 50%; background: rgba(20,28,52,0.55);
  }
  .hero-title {
    position: absolute; left: 0; right: 0; top: 150px;
    text-align: center; color: var(--hero-text);
    font-weight: 300; font-size: 32px; line-height: 38px; letter-spacing: 1px;
  }
  .hero-title strong { display: block; font-weight: 700; font-size: 40px; line-height: 44px; }

  .welcome { text-align: center; padding-top: 14px; }
  .welcome-title { font-family: "Roboto Condensed", Arial, sans-serif; font-weight: 700; font-size: 22px; }
  .welcome-title span { color: var(--red); }
  .welcome-rule { margin: 14px 48px 0; border-top: 1px dashed var(--red); }
  .welcome-text { font-size: 13px; line-height: 19px; margin: 16px auto 0; width: 1080px; }

  .service-tabs {
    position: absolute; left: 0; right: 0; bottom: 0; height: 64px;
    background: var(--grey-band);
    display: flex; justify-content: center; align-items: center; gap: 30px;
    font-family: "Roboto Condensed", Arial, sans-serif; font-weight: 700; font-size: 19px;
  }
  .service-tab { padding: 10px 18px; }
  .service-tab.is-active { color: var(--red); border: 1px solid var(--red); border-radius: 3px; background: var(--white); }
</style>
</head>
<body>
<div class="site">
  <header class="site-header">
    <div class="brand"><span class="brand-mark"></span><span class="brand-name">Tovi Electrical</span></div>
    <nav class="main-nav">
      <a href="#">Our Company</a>
      <a href="#">Services</a>
      <a href="#">Our Work</a>
      <a href="#">Contact</a>
    </nav>
    <div class="header-actions">
      <span class="chat-link">Chat
        <svg width="14" height="12" viewBox="0 0 14 12"><path d="M2 1h10a1 1 0 0 1 1 1v5a1 1 0 0 1-1 1H6l-3 3V8H2a1 1 0 0 1-1-1V2a1 1 0 0 1 1-1z" fill="none" stroke="#1b1b1b" stroke-width="1.3"/></svg>
      </span>
      <span class="call-button">Call: 13 7290</span>
    </div>
  </header>

  <section class="hero">
    <div class="hero-photo" role="img" aria-label="Modern architect-designed homes lit up at dusk with glowing windows and lawn"></div>
    <div class="hero-shade"></div>
    <div class="hero-circle"></div>
    <h1 class="hero-title">DO YOU<strong>NEED</strong>A<br>ELECTRICIAN</h1>
  </section>

  <section class="welcome">
    <h2 class="welcome-title">Welcome to <span>Tovi Electrical</span></h2>
    <div class="welcome-rule"></div>
    <p class="welcome-text">Tovi Electrical was formed to be an expert Electricity Contracting Company providing services to all Residential and Commercial Customers. With over 10 years of experience, Tovi Electrical has developed a highly-experienced team of professionals that ensure all our customer expectations are met.</p>
  </section>

  <nav class="service-tabs">
    <span class="service-tab is-active">Residential</span>
    <span class="service-tab">Commercial</span>
    <span class="service-tab">Property Management</span>
  </nav>
</div>
</body>
</html>
```